nutrition company business card

I would like to have a business card that has two sides, one being the green color from the Company name on the logo. I am open to ideas and looks that work with my logo. I like the idea of having a negative image of the tree on the green side.

For my information on the card I must have:
Linda Moorcombe
415-872-6041
lindamoorcombe@quellmail.net

This area will need to be updated once I complete my schooling.

Reason: I need to extend my deadline by one day as I have been sick the last week and not had time to review all the new designs. Thank you.

Industry/Entity Type

Nutrition

Requirements
Must have
• I would like to have a business card that has two sides, one being the green color from the Company name on the logo. I am open to ideas and looks that work with my logo. I like the idea of having a negative image of the tree on the green side.
• For my information on the card I must have:
• Linda Moorcombe
• 415-872-6041
• lindamoorcombe@quellmail.net
• This area will need to be updated once I complete my schooling.

```html
<!DOCTYPE html>
<html lang="en">
<head>
<meta charset="utf-8">
<title>Rooted Tables – Business Card</title>
<link rel="stylesheet" href="https://fonts.googleapis.com/css2?family=Quicksand:wght@400;500&family=Open+Sans:ital,wght@0,400;1,700&display=swap">
<style>
  :root {
    --canvas: #ece9e4;
    --card-white: #ffffff;
    --brand-green: #7fc241;
    --brand-green-deep: #72b536;
    --ink-grey: #7a726c;
    --faint-grey: #ececec;
    --faint-green: #74b33a;
    --text-white: #ffffff;
  }
  * { margin: 0; padding: 0; box-sizing: border-box; }
  html, body {
    width: 1200px; height: 1024px; overflow: hidden;
    background: var(--canvas);
  }
  .canvas { position: relative; width: 1200px; height: 1024px; }

  .card {
    position: absolute;
    width: 600px; height: 343px;
    border-radius: 24px;
    overflow: hidden;
    box-shadow: 0 6px 18px rgba(0,0,0,0.12);
  }
  .card--front { left: 90px; top: 110px; background: var(--card-white); }
  .card--back  { left: 510px; top: 570px; background: var(--brand-green); }

  .card__art { position: absolute; inset: 0; }

  .brand {
    position: absolute;
    display: flex; align-items: center; gap: 18px;
  }
  .brand__mark {
    width: 74px; height: 74px; border-radius: 50%;
    flex: none;
  }
  .brand__name {
    font-family: "Quicksand", sans-serif;
    font-weight: 400;
    font-size: 38px;
    line-height: 1;
    letter-spacing: 0.2px;
  }
  .brand__tagline {
    font-family: "Quicksand", sans-serif;
    font-weight: 400;
    font-size: 19px;
    letter-spacing: 1.2px;
    margin-top: 6px;
  }

  .card--front .brand { left: 34px; top: 70px; }
  .card--front .brand__mark { background: var(--brand-green); }
  .card--front .brand__name { color: var(--brand-green); }
  .card--front .brand__tagline { color: var(--ink-grey); }

  .card--back .brand { left: 50px; top: 92px; }
  .card--back .brand__mark { background: var(--text-white); }
  .card--back .brand__name { color: var(--text-white); }
  .card--back .brand__tagline { color: var(--text-white); }

  .contact {
    position: absolute; left: 128px; top: 226px;
    color: var(--text-white);
    font-family: "Open Sans", sans-serif;
  }
  .contact__name { font-weight: 700; font-style: italic; font-size: 20px; margin-bottom: 8px; }
  .contact__row {
    display: flex; align-items: center; gap: 8px;
    font-size: 16px; line-height: 1.55;
  }
  .contact__icon { width: 14px; height: 14px; flex: none; }
</style>
</head>
<body>
<main class="canvas">

  <section class="card card--front" aria-label="Business card front">
    <svg class="card__art" viewBox="0 0 600 343" aria-hidden="true">
      <circle class="decor-circle" cx="520" cy="50" r="98" fill="var(--faint-grey)"/>
      <path class="green-band" d="M0 200 L330 200 C420 200 455 175 490 118 L600 118 L600 343 L0 343 Z" fill="var(--brand-green)"/>
    </svg>

    <div class="brand">
      <span class="brand__mark"></span>
      <div class="brand__text">
        <div class="brand__name">Rooted Tables</div>
        <div class="brand__tagline">good food made simple</div>
      </div>
    </div>

    <div class="contact">
      <div class="contact__name">Linda Moorcombe</div>
      <div class="contact__row">
        <svg class="contact__icon" viewBox="0 0 24 24" aria-hidden="true"><path fill="#fff" d="M6.6 10.8a15.1 15.1 0 0 0 6.6 6.6l2.2-2.2c.3-.3.7-.4 1-.2 1.1.4 2.3.6 3.6.6.6 0 1 .4 1 1V20c0 .6-.4 1-1 1A17 17 0 0 1 3 4c0-.6.4-1 1-1h3.5c.6 0 1 .4 1 1 0 1.3.2 2.5.6 3.6.1.3 0 .7-.2 1z"/></svg>
        <span>415-872-6041</span>
      </div>
      <div class="contact__row">
        <svg class="contact__icon" viewBox="0 0 24 24" aria-hidden="true"><rect x="2" y="5" width="20" height="14" rx="1" fill="#fff"/><path d="M3 6l9 7 9-7" fill="none" stroke="var(--brand-green)" stroke-width="1.8"/></svg>
        <span>lindamoorcombe@quellmail.net</span>
      </div>
    </div>
  </section>

  <section class="card card--back" aria-label="Business card back">
    <svg class="card__art" viewBox="0 0 600 343" aria-hidden="true">
      <circle class="decor-circle" cx="430" cy="365" r="160" fill="var(--faint-green)"/>
    </svg>

    <div class="brand">
      <span class="brand__mark"></span>
      <div class="brand__text">
        <div class="brand__name">Rooted Tables</div>
        <div class="brand__tagline">good food made simple</div>
      </div>
    </div>
  </section>

</main>
</body>
</html>
```